Zielgruppe
Ich bin Fotograf und habe mich auf Schwangerschafts- und Neugeborenenfotografie spezialisiert. Meine Zielgruppe sind schwangere Frauen im letzten Drittel der Schwangerschaft und frisch gewordene Eltern.
Aufgabenstellung
- sehr schlichtes Design, in der Anlage finden Sie zwei der meist verkauften Karten damit Sie sich vom Stil eine Vorstellung machen können
- Lieferung als offene Indesign 5.5 Datei (so das die Farben, Texte, .... angepasst werden können)
- 2-3 Bilder (querformat) sollen in das Design eingearbeitet werden können
- Die Karten werden von mir nachher als fertig gedruckte Karte an meine Kunden verkauft, dies bitte ich zu berücksichtigen
- ich möchte die Karten so nutzen können das sowohl Geburtskarten für Jungs wie auch für Mädels erstellt werden können
- Format: Din A6 (geschlossen 105x148mm), Klappkarte, hoch, 3mm Beschnitt

```html
<!DOCTYPE html>
<html lang="de">
<head>
<meta charset="utf-8">
<title>Geburtskarte – Klappkarte A6</title>
<link href="https://fonts.googleapis.com/css2?family=Amatic+SC:wght@400;700&family=Jost:wght@300&family=Zilla+Slab:wght@300&display=swap" rel="stylesheet">
<style>
  :root {
    --bg: #f1f1f1;
    --teal: #a3c1bb;
    --slate: #6e6e6e;
    --paper: #ffffff;
    --label: #8a8a8a;
    --body-ink: #5e5e5e;
    --photo-dark: #1e1e1e;
    --photo-mid: #8c8c8c;
    --photo-light: #e4e4e4;
  }
  * { box-sizing: border-box; margin: 0; padding: 0; }
  html, body {
    width: 1200px; height: 829px; overflow: hidden;
    background: radial-gradient(ellipse at center, #fafafa 0%, var(--bg) 80%);
  }
  .stage {
    position: relative; width: 1200px; height: 829px;
  }
  .spread-group { position: absolute; top: 192px; width: 560px; }
  .spread-group--outside { left: 30px; }
  .spread-group--inside { left: 610px; }
  .labels { display: flex; height: 34px; }
  .labels span {
    flex: 1; text-align: center;
    font-family: 'Jost', sans-serif; font-weight: 300;
    font-size: 21px; color: var(--label); letter-spacing: 0.5px;
  }
  .spread { display: flex; width: 560px; height: 395px; }
  .page { position: relative; width: 280px; height: 395px; overflow: hidden; }

  .display {
    font-family: 'Amatic SC', sans-serif; font-weight: 400;
    color: var(--paper); text-align: center; line-height: 1;
  }
  .photo { position: absolute; left: 0; width: 280px; }

  /* Rückseite */
  .back { background: var(--slate); }
  .credit {
    position: absolute; left: 104px; bottom: 13px;
    font-family: 'Jost', sans-serif; font-weight: 300;
    font-size: 6.5px; color: #dcdcdc;
  }

  /* Vorderseite */
  .front { background: var(--slate); }
  .front .name-band {
    position: absolute; top: 0; left: 0; width: 280px; height: 82px;
    background: var(--teal);
    display: flex; align-items: center; justify-content: center;
  }
  .front .name-band .display { font-size: 46px; letter-spacing: 2px; }
  .front .photo {
    top: 84px; height: 227px;
    background: radial-gradient(ellipse at 68% 45%, var(--photo-mid) 0%, #3a3a3a 45%, var(--photo-dark) 80%);
  }
  .front .date-block {
    position: absolute; top: 322px; left: 0; width: 280px; text-align: center;
  }
  .front .date { font-size: 30px; letter-spacing: 1px; }
  .front .city { font-size: 21px; letter-spacing: 1.5px; margin-top: 2px; }

  /* Innenseite links */
  .inner-left .photo {
    top: 0; height: 217px;
    background: radial-gradient(ellipse at 50% 50%, #9a9a9a 0%, #cfcfcf 55%, var(--photo-light) 100%);
  }
  .inner-left .announce {
    position: absolute; top: 219px; left: 0; width: 280px; height: 176px;
    background: var(--teal);
    display: flex; align-items: center; justify-content: center;
  }
  .inner-left .announce .display { font-size: 50px; letter-spacing: 2px; line-height: 0.98; }

  /* Innenseite rechts */
  .inner-right { background: var(--paper); }
  .inner-right .verse {
    position: absolute; top: 26px; left: 0; width: 280px; text-align: center;
    font-family: 'Amatic SC', sans-serif; font-weight: 400;
    font-size: 22px; line-height: 1.04; color: var(--teal); letter-spacing: 1px;
  }
  .inner-right .thanks {
    position: absolute; top: 144px; left: 0; width: 280px; text-align: center;
    font-family: 'Zilla Slab', serif; font-weight: 300;
    font-size: 11.5px; line-height: 1.55; color: var(--body-ink);
  }
  .inner-right .photo {
    top: 219px; height: 176px;
    background: radial-gradient(ellipse at 60% 55%, #a5a5a5 0%, #d4d4d4 50%, var(--photo-light) 100%);
  }
</style>
</head>
<body>
<main class="stage">

  <section class="spread-group spread-group--outside">
    <div class="labels"><span>Rückseite</span><span>Vorderseite</span></div>
    <div class="spread">
      <div class="page back">
        <p class="credit">Lindholm Fotografie</p>
      </div>
      <div class="page front">
        <div class="name-band"><h1 class="display">Mattis</h1></div>
        <div class="photo" role="img" aria-label="Schwarzweißfoto: Neugeborenes liegt auf den Händen der Eltern"></div>
        <div class="date-block">
          <p class="display date">09.03.2016</p>
          <p class="display city">Hamburg</p>
        </div>
      </div>
    </div>
  </section>

  <section class="spread-group spread-group--inside">
    <div class="labels"><span>Innenseite links</span><span>Innenseite rechts</span></div>
    <div class="spread">
      <div class="page inner-left">
        <div class="photo" role="img" aria-label="Schwarzweißfoto: Porträt eines Neugeborenen in eine Decke gehüllt"></div>
        <div class="announce"><p class="display">Mattis<br>ist da!</p></div>
      </div>
      <div class="page inner-right">
        <p class="verse">Manches beginnt klein,<br>manches beginnt groß,<br>aber manchmal ist das<br>Kleinste das Größte</p>
        <p class="thanks">Danke für all die<br>Glückwünsche und Geschenke!<br>Frida &amp; Jonte</p>
        <div class="photo" role="img" aria-label="Schwarzweißfoto: schlafendes Neugeborenes auf einer Decke"></div>
      </div>
    </div>
  </section>

</main>
</body>
</html>
```